Bold Flyer Needed for Bold Little Gym

We need a 1 page flyer created for our small boutique fitness facility, GymVorel, which highlights a new service we are offering.
We are now offering Red Light Therapy (RLT) to our members and I need a full color, 1 page flyer created that captures the eye of our members while highlighting the benefits and clearly stating the prices at the bottom of the page.
Flyer will be printed out on a standard 8.5" x 11" sheet of paper and should be laid out in a way that is easy to read. Landscape or Portrait layouts are both expectable.
We are using Cobalt Glow Wellness Lights LumaCore 700 Lamps as found here http://lnk.example-short.net/7QWZT4R
I have attached the text that should be included and our logo for branding of the flyer.
Thank you!
Look and feel
Each slider illustrates characteristics of the customer's brand and the style your logo design should communicate.

```html
<!DOCTYPE html>
<html lang="en">
<head>
<meta charset="utf-8">
<title>GymVorel – Red Light Therapy</title>
<link href="https://fonts.googleapis.com/css2?family=Baloo+2:wght@400;500;600;700;800&family=Hind:wght@300;400;500;600&display=swap" rel="stylesheet">
<style>
:root{
  --ink:#0f0605;
  --glow:#2a1806;
  --yellow:#f6cf0b;
  --red:#d6363c;
  --band:#c8313a;
  --white:#ffffff;
  --row:#f1f1f1;
  --text:#1c1c1c;
  --head:"Baloo 2", sans-serif;
  --body:"Hind", sans-serif;
}
*{margin:0;padding:0;box-sizing:border-box}
html,body{width:927px;height:1200px;overflow:hidden;background:var(--ink)}
.flyer{position:relative;width:927px;height:1200px;overflow:hidden;color:var(--white);font-family:var(--body);
  background:radial-gradient(ellipse 520px 520px at 260px 560px,var(--glow),var(--ink) 75%)}
.abs{position:absolute}
.hero-photo{left:530px;top:21px;width:450px;height:450px;border-radius:50%;
  background:radial-gradient(circle at 50% 50%,#8a0c0a 0%,#3a0404 30%,#7a1a14 36%,#d8452f 52%,#e8782a 72%,#f2b418 100%)}
.panel-photo{left:848px;top:68px;width:74px;height:272px;border-radius:4px;
  background:linear-gradient(90deg,#f3eded,#f6c6c6 40%,#ef9b9b 70%,#d8d8d8)}
.brand{left:45px;top:18px}
.brand-name{font-family:var(--head);font-weight:800;font-size:68px;line-height:1;color:var(--yellow);letter-spacing:1px}
.brand-tag{font-family:var(--head);font-weight:700;font-size:9.5px;letter-spacing:2.6px;color:var(--yellow);margin:4px 0 0 48px}
.h-main{font-family:var(--head);font-weight:700;font-size:23px;line-height:30px;color:var(--white)}
.h-red{color:var(--red)}
.h-yellow{font-family:var(--head);font-weight:700;color:var(--yellow)}
.benefits-title{left:43px;top:340px;font-size:26px;line-height:30px}
.benefits{left:44px;top:418px;width:312px;list-style:none;font-size:12.6px;line-height:21px}
.benefits b{font-weight:600}
.rule{left:41px;top:682px;width:353px;height:1px;background:var(--red)}
.about-title{left:44px;top:696px;font-size:21px}
.about{left:44px;top:724px;width:350px;font-size:14.3px;line-height:22px;font-weight:300}
.facility{left:460px;top:495px;font-family:var(--head);font-weight:700;font-size:30px;line-height:35px}
.prices{left:459px;top:622px;width:431px;border-collapse:collapse;font-family:var(--head);color:var(--text)}
.prices th{background:var(--yellow);height:45px;font-size:17px;font-weight:700;color:var(--text)}
.prices td{height:43px;text-align:center;font-size:19px;font-weight:500;border-left:1px solid #ddd}
.prices td:first-child{text-align:left;padding-left:18px;font-family:var(--body);font-size:11px;font-weight:400;border-left:none}
.prices tr:nth-child(odd) td{background:var(--white)}
.prices tr:nth-child(even) td{background:var(--row)}
.why-title{left:0;width:927px;top:882px;text-align:center;font-size:23px}
.feature{top:935px}
.feature .ico{position:absolute;left:0;top:0;width:54px;height:54px}
.feature h3{position:absolute;left:74px;top:0;font-family:var(--head);font-weight:700;font-size:14px;white-space:nowrap}
.feature p{position:absolute;left:74px;top:22px;font-size:10.5px;line-height:16.5px;font-weight:300}
.offer-title{top:1027px;font-size:22px}
.offer-text{top:1066px;font-size:14.6px;line-height:24px}
.cta{left:0;top:1140px;width:927px;height:60px;background:var(--band);display:flex;align-items:center}
.cta strong{font-family:var(--head);font-weight:700;font-size:21px;margin-left:48px;width:232px}
.cta span{font-size:16.3px}
.cta span b{font-weight:600}
</style>
</head>
<body>
<div class="flyer">

  <div class="abs hero-photo" role="img" aria-label="Photo of a person in profile bathed in red light, framed in warm orange tones"></div>
  <div class="abs panel-photo" role="img" aria-label="Red light therapy panel with rows of LEDs"></div>

  <div class="abs brand">
    <div class="brand-name">GymVorel</div>
    <div class="brand-tag">PERSONAL GROUP TRAINING</div>
  </div>

  <h1 class="abs h-main" style="left:44px;top:141px">Unlock Your Potential with Red Light<br>Therapy at GymVorel!</h1>
  <h2 class="abs h-main" style="left:44px;top:215px">Introducing Our New Red Light Therapy Room!</h2>
  <h2 class="abs h-main" style="left:44px;top:261px">Transform Your Wellness Routine with the<br><span class="h-red">Power of Light!</span></h2>

  <h2 class="abs h-yellow benefits-title">Benefits of<br>Red Light Therapy</h2>
  <ul class="abs benefits">
    <li>• <b>Boosts Energy Levels:</b> Feel revitalized and more energetic after each session.</li>
    <li>• <b>Enhances Muscle Recovery:</b> Speed up recovery times post-workout and reduce soreness.</li>
    <li>• <b>Improves Skin Health:</b> Reduce wrinkles, blemishes, and promote a youthful glow.</li>
    <li>• <b>Supports Joint Health:</b> Alleviate pain and inflammation, making movement easier.</li>
    <li>• <b>Promotes Better Sleep:</b> Improve your sleep patterns and overall restfulness.</li>
    <li>• <b>Increases Circulation:</b> Enhance blood flow for better nutrient delivery to muscles.</li>
  </ul>

  <div class="abs rule"></div>
  <h2 class="abs h-yellow about-title">What is Red Light Therapy?</h2>
  <p class="abs about">Red Light Therapy (RLT) is a revolutionary treatment that uses specific wavelengths of light to promote healing, reduce inflammation, and enhance overall well-being. At GymVorel, we are excited to offer the advanced Cobalt Glow Wellness LumaCore 700 panels—designed to maximize your health benefits in a relaxing environment.</p>

  <h2 class="abs facility">GymVorel Fitness Facility,<br>Your Wellness, Our<br>Commitment!</h2>

  <table class="abs prices">
    <colgroup><col style="width:102px"><col style="width:177px"><col style="width:152px"></colgroup>
    <thead><tr><th>PRICES</th><th>GymVorel Member</th><th>Non-Member</th></tr></thead>
    <tbody>
      <tr><td>Single Session</td><td>$35</td><td>$55</td></tr>
      <tr><td>3 – Pack</td><td>$102</td><td>$159</td></tr>
      <tr><td>5 – Pack</td><td>$167</td><td>$259</td></tr>
      <tr><td>10 – Pack</td><td>$316</td><td>$491</td></tr>
    </tbody>
  </table>

  <h2 class="abs h-yellow why-title">Why Choose GymVorel?</h2>

  <div class="abs feature" style="left:47px;width:280px">
    <svg class="ico" viewBox="0 0 54 54" aria-hidden="true">
      <circle cx="27" cy="27" r="25" fill="none" stroke="var(--red)" stroke-width="3"/>
      <g fill="none" stroke="#fff" stroke-width="1.5"><rect x="16" y="16" width="10" height="8"/><rect x="29" y="18" width="9" height="7"/><path d="M21 24v14M26 30h8M21 38h4"/></g>
    </svg>
    <h3>State-of-the-Art Equipment</h3>
    <p>Experience the power of eight Cobalt Glow Wellness LumaCore 700 panels—some of the best on the market!</p>
  </div>

  <div class="abs feature" style="left:328px;width:300px">
    <svg class="ico" viewBox="0 0 54 54" aria-hidden="true">
      <circle cx="27" cy="27" r="25" fill="none" stroke="var(--red)" stroke-width="3"/>
      <g fill="none" stroke="#fff" stroke-width="1.5"><circle cx="27" cy="24" r="10"/><path d="M27 18l2 4 4 .5-3 3 .8 4-3.8-2-3.8 2 .8-4-3-3 4-.5z"/><path d="M21 32l-4 8 5-1 2 4 3-7M33 32l4 8-5-1-2 4-3-7"/></g>
    </svg>
    <h3>Expert Guidance</h3>
    <p>Our trained staff will guide you through each session to ensure you get the most out of your therapy.</p>
  </div>

  <div class="abs feature" style="left:628px;width:295px">
    <svg class="ico" viewBox="0 0 54 54" aria-hidden="true">
      <circle cx="27" cy="27" r="25" fill="none" stroke="var(--red)" stroke-width="3"/>
      <g fill="none" stroke="#fff" stroke-width="1.5"><circle cx="27" cy="22" r="3"/><circle cx="18" cy="29" r="3.5"/><circle cx="36" cy="29" r="3.5"/><path d="M22 36c2-5 8-5 10 0M24 30h6"/></g>
    </svg>
    <h3>Community Focused</h3>
    <p>Join a supportive community that prioritizes health and wellness.</p>
  </div>

  <h2 class="abs h-yellow offer-title" style="left:47px">Special Introductory Offer!</h2>
  <p class="abs offer-text" style="left:48px">Try Your First Session for Just $25!<br>(Regularly $55)</p>

  <h2 class="abs h-yellow offer-title" style="left:394px">Limited Time Only!</h2>
  <p class="abs offer-text" style="left:394px;width:500px">Book your session today and discover how Red Light Therapy can elevate your fitness</p>

  <div class="abs cta">
    <strong>Ready to Shine?</strong>
    <span>Visit our front desk or call us at <b>(555) 014-2890</b> to schedule your appointment.</span>
  </div>
</div>
</body>
</html>
```